Corporate Branded Documents - IT Provider - On-going work

Hi, I'm Neil a Director of Harbourline Tech Care a UK Based IT & Telecoms support firm. We've been trading for 12 years now and feel its time for a lick of paint. We have a logo, website etc but would like someone to create some standard documents for us.

- A PDF Proposal Template - We currently don't send our customers proposals as we have nothing that looks good.
- A Quote Template PDF - Example Attached
- A Order Template PDF - Example Attached
- A Invoice Template PDF - Example Attached
- A Generic Document PDF - Something we can use for customer application forms, NDA Agreements, Terms & Conditions etc

Our website can be found at www.harbourlinetechcare.co.uk - here you'll get a feel for our branding. I've also attached 2 example documents - as well as our currently used documents. Hopefully you guys can see why it needs improving.

We'd also like to work with someone long term, these documents are a start but we'd like to make sure all the work we do looks and feels as smart as possible, so there is plenty of additional work available.

None of these templates need to be Print ready, 99% of the time it will be viewed digitally, so high resolution designs are best

Thanks,

Neil

Target Market(s)

Corporate & Educational Customers

Industry/Entity Type

It Support

Font styles to use
Sans Serif

Colors
ec1f27
0692cd
ffffff

```html
<!DOCTYPE html>
<html lang="en">
<head>
<meta charset="utf-8">
<title>Harbourline Tech Care – Tax Invoice</title>
<link href="https://fonts.googleapis.com/css2?family=Open+Sans:wght@400;600;700&family=Montserrat:wght@600;700&display=swap" rel="stylesheet">
<style>
  :root {
    --brand-red: #e0232b;
    --brand-teal: #1e7f97;
    --link-blue: #1a2fd8;
    --ink: #2b2b2b;
    --paper: #ffffff;
    --backdrop: #eceae6;
  }
  * { box-sizing: border-box; margin: 0; padding: 0; }
  html, body { width: 1200px; height: 743px; overflow: hidden; background: var(--backdrop); }
  body { font-family: "Open Sans", Arial, sans-serif; color: var(--ink); }

  .invoice-sheet {
    position: absolute; left: 345px; top: 11px;
    width: 510px; height: 721px;
    background: var(--paper);
    box-shadow: 0 4px 18px rgba(0,0,0,.15);
    overflow: hidden;
  }
  .header-art {
    position: absolute; left: 0; top: 0; width: 100%; height: 150px;
    background:
      linear-gradient(180deg, rgba(255,255,255,0) 55%, #fff 100%),
      linear-gradient(100deg, #fbf6c9 0%, #fcefc0 35%, #f9dfe3 70%, #f6d3e4 100%);
  }
  .brand-name {
    position: absolute; left: 34px; top: 58px;
    font-family: "Open Sans", Arial, sans-serif; font-weight: 700;
    font-size: 16px; color: var(--ink);
  }
  .sender {
    position: absolute; left: 318px; top: 42px;
    font-style: normal;
    font-size: 7.5px; line-height: 9.5px; color: var(--ink);
  }
  .sender strong { font-weight: 700; }

  .invoice-meta { position: absolute; left: 34px; top: 158px; }
  .doc-title {
    font-family: "Montserrat", Arial, sans-serif; font-weight: 700;
    font-size: 15px; color: var(--brand-red); letter-spacing: .5px;
  }
  .meta-list { list-style: none; font-size: 7.5px; line-height: 9.5px; margin-top: 2px; }

  .terms { position: absolute; left: 34px; top: 488px; width: 460px; }
  .terms h2 {
    font-family: "Montserrat", Arial, sans-serif; font-weight: 700;
    font-size: 12px; color: var(--brand-red); margin-bottom: 3px;
  }
  .terms p { font-size: 7px; line-height: 10px; white-space: nowrap; }
  .terms a { color: var(--link-blue); text-decoration: none; }

  .footer-band { position: absolute; left: 0; bottom: 0; width: 100%; height: 160px; }
  .footer-band svg { position: absolute; inset: 0; }
  .payment-options {
    position: absolute; left: 34px; bottom: 22px; color: #fff;
    font-size: 8.5px; line-height: 12px;
  }
  .payment-options h3 {
    font-family: "Montserrat", Arial, sans-serif; font-weight: 600;
    font-size: 13px; margin-bottom: 3px;
  }
  .payment-options b { font-weight: 700; }
  .footer-divider {
    position: absolute; left: 300px; bottom: 30px; width: 1px; height: 70px;
    background: rgba(255,255,255,.6);
  }
  .registration {
    position: absolute; left: 318px; bottom: 58px; width: 175px;
    color: #fff; font-size: 7.5px; line-height: 10px;
  }
</style>
</head>
<body>
  <main class="invoice-sheet">
    <div class="header-art" role="img" aria-label="Soft pastel geometric triangle pattern in yellow and pink"></div>

    <p class="brand-name">Harbourline Tech Care</p>

    <address class="sender">
      <strong>Harbourline Tech Care Ltd</strong><br>
      Phone: 0113 496 0182<br>
      Email: licensing@harbourlinetechcare.co.uk<br>
      Address: 27 Quayside Row<br>
      Leeds<br>
      West Yorkshire<br>
      LS10 4TR<br>
      UNITED KINGDOM
    </address>

    <section class="invoice-meta">
      <h1 class="doc-title">TAX INVOICE</h1>
      <ul class="meta-list">
        <li>Invoice Number: INV-13642</li>
        <li>Invoice Date: 25 Mar 2018</li>
        <li>Account Number:</li>
        <li>Reference:</li>
      </ul>
    </section>

    <section class="terms">
      <h2>Terms &amp; Conditions</h2>
      <p>By clicking "Agree &amp; Buy" you confirm that you've read and agree to Northgate Soft's <a href="#">Privacy Policy</a> and <a href="#">End User License Agreement</a>.<br>
      You have the right to cancel and receive a refund in accordance with applicable conditions.</p>
    </section>

    <footer class="footer-band">
      <svg viewBox="0 0 510 160" preserveAspectRatio="none" aria-hidden="true">
        <path d="M0 52 Q255 -6 510 14 L510 160 L0 160 Z" fill="var(--brand-red)"/>
        <path d="M0 60 Q255 4 510 22 L510 160 L0 160 Z" fill="var(--brand-teal)"/>
      </svg>
      <div class="payment-options">
        <h3>Payment Options</h3>
        <b>Bank Name:</b> Meridian Banking Group (UK)<br>
        <b>Account Number:</b> 01928374<br>
        <b>Sort Code:</b> 20-44-17
      </div>
      <span class="footer-divider"></span>
      <p class="registration">Company Registration No: 07731462. Registered Office: 27 Quayside Row, Leeds, West Yorkshire, LS10 4TR, United Kingdom</p>
    </footer>
  </main>
</body>
</html>
```